Logo and business card for optometric practice
Curtis Hallorann & Associates
Marta Pelovska, O.D.
Oscar Tremwitz, O.D.
Neil Borromi, O.D.
417 Pembrook Parkway
Ashcombe Falls, Ohio 44871
516-902-4471

Target Market(s)

Patients, general public

Industry/Entity Type

Business

Logo Text

Curtis Hallorann & Associates Optometrists

Logo styles of interest
Pictorial/Combination Logo
Font styles to use
Serif
Sans Serif

Requirements
Must have
• current inspiration: realistic or photo closeup of eye, with interesting treatment of the iris OR
tech look, with closeup of eye and grid like the doctor is looking through a camera or microscope to view the eye up close
Should not have
• NO cartoons

```html
<!DOCTYPE html>
<html lang="en">
<head>
<meta charset="utf-8">
<title>Curtis Hallorann &amp; Associates — Business Card</title>
<link rel="stylesheet" href="https://fonts.googleapis.com/css2?family=Tinos:wght@400&display=swap">
<style>
  :root {
    --frame-blue: #29abe2;
    --brand-teal: #1a6f97;
    --ink: #111111;
    --paper: #ffffff;
  }
  html, body {
    margin: 0;
    padding: 0;
    width: 1200px;
    height: 686px;
    overflow: hidden;
    background: var(--paper);
  }
  .business-card {
    position: relative;
    width: 1200px;
    height: 686px;
    background: var(--paper);
    font-family: "Tinos", "Times New Roman", serif;
    color: var(--ink);
  }
  .card-frame {
    position: absolute;
    left: 25px;
    top: 18px;
    width: 1150px;
    height: 647px;
    box-sizing: border-box;
    border: 13px solid var(--frame-blue);
  }
  .brand-mark {
    position: absolute;
    left: 62px;
    top: 296px;
    display: flex;
    align-items: center;
    gap: 16px;
  }
  .brand-mark__dot {
    width: 86px;
    height: 86px;
    border-radius: 50%;
    background: var(--brand-teal);
  }
  .brand-mark__name {
    font-size: 34px;
    line-height: 1;
    color: var(--brand-teal);
    white-space: nowrap;
  }
  .practice-name {
    position: absolute;
    left: 442px;
    top: 222px;
    margin: 0;
    font-weight: 400;
    font-size: 52px;
    line-height: 1;
    white-space: nowrap;
  }
  .doctor-list {
    position: absolute;
    left: 522px;
    top: 291px;
    margin: 0;
    padding: 0;
    list-style: none;
    font-size: 32px;
    line-height: 46px;
  }
  .contact-block {
    position: absolute;
    left: 0;
    right: 0;
    top: 582px;
    text-align: center;
    font-size: 21px;
    line-height: 29px;
    font-style: normal;
  }
  .contact-block p {
    margin: 0;
    transform: translateX(-3px);
  }
</style>
</head>
<body>
  <main class="business-card">
    <div class="card-frame"></div>

    <div class="brand-mark">
      <span class="brand-mark__dot"></span>
      <span class="brand-mark__name">Curtis Hallorann</span>
    </div>

    <h1 class="practice-name">Curtis Hallorann &amp; Associates</h1>

    <ul class="doctor-list">
      <li>Marta Pelovska, O.D.</li>
      <li>Oscar Tremwitz, O.D.</li>
      <li>Neil Borromi, O.D.</li>
    </ul>

    <address class="contact-block">
      <p class="contact-address">417 Pembrook Parkway, Ashcombe Falls, Ohio, 44871</p>
      <p class="contact-phone">516-902-4471</p>
    </address>
  </main>
</body>
</html>
```